Swimming Pool Supply Company Business Cards

We need business cards designed for company. These need to be easy to edit so that we can fill in names, titles, and contact info for each person who works here.

Dalton R. Whitfield
Manager of Legal & Finance
K.L. Brisbane, Incorporated

4837 Grenway Avenue
Marlow Heights, PA 19243

E. dalton@klbrisbane-example.com
M. (215) 555-0173
O. (215) 555-0148

Contact Information for Business Card

Looking to upgrade current business cards with graphic that can be edited. Looking for fresh ideas for an age old industry.

Font styles to use
Serif
Sans Serif

Colors

Designer to choose colors to be used in the design.

Requirements
Must have
• Professional, fresh, unique but professional

```html
<!DOCTYPE html>
<html lang="en">
<head>
<meta charset="utf-8">
<title>K.L. Brisbane Business Card – Dalton R. Whitfield</title>
<link rel="stylesheet" href="https://fonts.googleapis.com/css2?family=Source+Sans+3:wght@400;700&display=swap">
<style>
  :root {
    --ink: #000000;
    --paper: #ffffff;
    --page: #ffffff;
  }
  html, body {
    margin: 0;
    padding: 0;
    width: 720px;
    height: 1200px;
    overflow: hidden;
    background: var(--page);
  }
  .card {
    position: relative;
    width: 720px;
    height: 1200px;
    background: var(--paper);
    border-radius: 32px;
    overflow: hidden;
    font-family: "Source Sans 3", "Myriad Pro", Arial, sans-serif;
    color: var(--ink);
    text-align: center;
  }
  .header-band {
    position: absolute;
    left: 0; top: 0;
    width: 720px; height: 464px;
    background: var(--ink);
    color: var(--paper);
  }
  .person-name {
    position: absolute;
    left: 0; right: 0; top: 206px;
    margin: 0;
    font-size: 46px;
    font-weight: 400;
    line-height: 1;
  }
  .person-role, .company-name {
    position: absolute;
    left: 0; right: 0;
    margin: 0;
    font-size: 23px;
    line-height: 1;
  }
  .person-role { top: 265px; }
  .company-name { top: 298px; }

  .contact-group {
    position: absolute;
    left: 0; right: 0;
    font-size: 26px;
    line-height: 36px;
  }
  .contact-group p { margin: 0; }
  .contact-icon { display: block; margin: 0 auto 4px; fill: var(--ink); }
  .phone-group { top: 530px; }
  .mail-group { top: 683px; }
  .place-group { top: 787px; }

  .brand-name {
    position: absolute;
    left: 0; right: 0; top: 1004px;
    margin: 0;
    font-size: 104px;
    font-weight: 700;
    letter-spacing: 4px;
    line-height: 1;
  }
  .footer-band {
    position: absolute;
    left: 0; bottom: 0;
    width: 720px; height: 58px;
    background: var(--ink);
  }
</style>
</head>
<body>
  <main class="card">
    <header class="header-band">
      <h1 class="person-name">Dalton R. Whitfield</h1>
      <p class="person-role">Manager of Legal &amp; Finance</p>
      <p class="company-name">K.L. Brisbane, Incorporated</p>
    </header>

    <section class="contact-group phone-group">
      <svg class="contact-icon" width="46" height="32" viewBox="0 0 46 32" aria-hidden="true">
        <path d="M2 9 C2 3 10 1 23 1 C36 1 44 3 44 9 L44 12 L34 12 L34 8 L12 8 L12 12 L2 12 Z"/>
        <path d="M14 10 L32 10 L40 30 L6 30 Z"/>
        <circle cx="23" cy="20" r="6" fill="#fff"/>
        <circle cx="23" cy="20" r="2.5"/>
      </svg>
      <p>M. (215) 555-0173</p>
      <p>O. (215) 555-0148</p>
    </section>

    <section class="contact-group mail-group">
      <svg class="contact-icon" width="40" height="28" viewBox="0 0 40 28" aria-hidden="true">
        <path d="M1 1 H39 V27 H1 Z M4 4 L20 17 L36 4 Z M3 6 V24 L14 14 Z M37 6 V24 L26 14 Z M16 16 L4 25 H36 L24 16 L20 19.5 Z" fill-rule="evenodd"/>
      </svg>
      <p>dalton@klbrisbane-example.com</p>
    </section>

    <section class="contact-group place-group">
      <svg class="contact-icon" width="30" height="42" viewBox="0 0 30 42" aria-hidden="true">
        <path d="M15 1 C7 1 1 7 1 15 C1 25 15 41 15 41 C15 41 29 25 29 15 C29 7 23 1 15 1 Z M15 9 A6 6 0 1 0 15.01 9 Z" fill-rule="evenodd"/>
      </svg>
      <p>4837 Grenway Avenue</p>
      <p>Marlow Heights, PA 19243</p>
    </section>

    <p class="brand-name">BRISBANE</p>

    <footer class="footer-band"></footer>
  </main>
</body>
</html>
```